Modern Corvane Tree Care Website

I need a website for a full service Tree Care company. The company provides tree pruning, tree removal, tree preservation, emergency services, stump grinding, and emergency tree services.

Target Market(s)

Customers that need tree services

Industry/Entity Type

Landscaping, Tree Services

Coding

Coded - Design and coding required

Number of Pages Required

5+ page

Font styles to use
Sans Serif

Requirements
Must have
• Good clean design that showcases the services the company provides.
Nice to have
• Services page; contact form, blog, home page, about page

```html
<!DOCTYPE html>
<html lang="en">
<head>
<meta charset="utf-8">
<title>Corvane Tree Care</title>
<link rel="stylesheet" href="https://fonts.googleapis.com/css2?family=Poppins:wght@400;500;600;700;800&display=swap">
<style>
:root{
  --navy:#201f3a;
  --green:#83c341;
  --white:#ffffff;
  --text:#4a4a55;
}
*{margin:0;padding:0;box-sizing:border-box}
html,body{width:1200px;height:2269px;overflow:hidden;background:var(--navy)}
body{font-family:"Poppins",sans-serif}
.stage{position:absolute;left:0;top:0;width:1234px;height:2333px;transform:scale(0.97245);transform-origin:0 0}
.page{position:absolute;left:44px;top:53px;width:1146px;height:2227px;background:var(--white);overflow:hidden}
.abs{position:absolute}

.hero{left:0;top:0;width:1146px;height:567px;background:
  radial-gradient(ellipse at 78% 40%,#8a5a3a 0,#6b4a30 25%,transparent 55%),
  linear-gradient(135deg,#3f4a2c 0%,#5a5236 40%,#6d5a42 70%,#4a3a2c 100%)}
.hero::after{content:"";position:absolute;inset:0;background:linear-gradient(90deg,rgba(20,20,20,.45),rgba(20,20,20,.1))}
.brand{display:flex;align-items:center;gap:7px;font-weight:700;color:var(--green);font-size:15px;letter-spacing:.3px}
.brand-mark{width:14px;height:14px;background:var(--green)}
.nav{z-index:2}
.nav-link{position:absolute;top:31px;color:var(--white);font-size:10.5px;font-weight:500}
.btn{display:inline-flex;align-items:center;justify-content:center;background:var(--green);color:var(--white);font-weight:600;font-size:9px}
.hero-title{left:191px;top:170px;z-index:2;color:var(--white);font-size:48px;font-weight:700;line-height:48px;letter-spacing:-.3px}
.hero-title em{font-style:normal;color:var(--green)}
.hero-sub{left:191px;top:335px;z-index:2;color:var(--white);font-size:14.5px}

.section-title{left:0;width:1146px;top:647px;text-align:center;color:var(--navy);font-size:24px;font-weight:700;line-height:34px}
.card{width:179px;height:179px;background:var(--navy);clip-path:polygon(38px 0,100% 0,100% 100%,0 100%,0 76px);color:var(--white);text-align:center}
.card-icon{position:absolute;left:64px;top:40px;width:52px;height:52px;border-radius:8px;background:linear-gradient(160deg,#83c341,#5f9230)}
.card-label{position:absolute;left:0;right:0;top:106px;font-size:16.5px;font-weight:600;line-height:20px}

.about-title{left:199px;top:1214px;color:var(--green);font-size:24px;font-weight:700}
.about-copy{left:199px;top:1264px;width:332px;color:var(--text);font-size:11.6px;line-height:16.8px}
.about-copy p+p{margin-top:16px}
.about-media{left:556px;top:1195px;width:400px;height:390px;border-radius:10px;background:linear-gradient(135deg,#7d8a5c 0%,#5c5a40 50%,#8e8a70 100%)}

.why{left:0;top:1605px;width:1146px;height:568px;background:
  radial-gradient(ellipse at 70% 50%,#5a4a38 0,#4d4230 20%,transparent 45%),
  linear-gradient(120deg,#5d6e44 0%,#8e9b78 30%,#6c7a52 55%,#a6ae94 80%,#5d6a40 100%)}
.why-panel{left:199px;top:1712px;width:315px;height:355px;background:rgba(30,30,30,.72)}
.why-title{position:absolute;left:49px;top:48px;color:var(--green);font-size:24px;font-weight:700}
.why-list{position:absolute;left:48px;top:104px;list-style:none}
.why-list li{display:flex;align-items:center;gap:17px;height:30px;color:var(--white);font-size:11.5px;font-weight:500}
.why-list li::before{content:"";width:15px;height:15px;background:var(--green);clip-path:polygon(50% 0,100% 100%,0 100%)}

.footer{left:0;top:2173px;width:1146px;height:54px;background:var(--white)}
.phones{position:absolute;right:191px;top:21px;display:flex;align-items:center;gap:6px;color:var(--navy);font-size:10.5px}
</style>
</head>
<body>
<div class="stage">
<main class="page">

  <section class="abs hero" role="img" aria-label="Photo of an arborist cutting a log with a chainsaw, sawdust flying"></section>

  <header class="abs nav" style="left:0;top:0;width:1146px;height:70px">
    <div class="abs brand" style="left:199px;top:29px"><span class="brand-mark"></span>Corvane Tree Care</div>
    <a class="nav-link" style="left:573px">Home</a>
    <a class="nav-link" style="left:628px">About Us</a>
    <a class="nav-link" style="left:700px">Services</a>
    <a class="nav-link" style="left:767px">Contact</a>
    <a class="abs btn" style="left:838px;top:25px;width:117px;height:24px">Get a FREE Estimate</a>
  </header>

  <h1 class="abs hero-title">Call <em>CORVANE</em> for<br>All Your Care<br>Need</h1>
  <p class="abs hero-sub">Serving Lafayette and Surrounding areas</p>

  <svg class="abs" style="left:0;top:567px" width="1146" height="70" viewBox="0 0 1146 70">
    <path d="M0 13 H800 C900 13 960 25 1011 66 L1003 66 C950 36 890 28 800 28 H0 Z" fill="var(--green)"/>
  </svg>

  <h2 class="abs section-title">Serving Lafayette<br>and Surrounding areas</h2>

  <div class="abs card" style="left:199px;top:749px"><span class="card-icon" role="img" aria-label="Tree trimming icon"></span><div class="card-label">Tree<br>Trimming</div></div>
  <div class="abs card" style="left:392px;top:749px"><span class="card-icon" role="img" aria-label="Tree preservation icon"></span><div class="card-label">Tree<br>Preservation</div></div>
  <div class="abs card" style="left:584px;top:749px"><span class="card-icon" role="img" aria-label="Tree removal icon"></span><div class="card-label">Tree<br>Removal</div></div>
  <div class="abs card" style="left:776px;top:749px"><span class="card-icon" role="img" aria-label="Tree cleaning icon"></span><div class="card-label">Tree<br>Cleaning</div></div>
  <div class="abs card" style="left:199px;top:942px"><span class="card-icon" role="img" aria-label="Tree pruning icon"></span><div class="card-label">Tree<br>Pruning</div></div>
  <div class="abs card" style="left:392px;top:942px"><span class="card-icon" role="img" aria-label="Stump grinding icon"></span><div class="card-label">Stump<br>Grinding</div></div>
  <div class="abs card" style="left:584px;top:942px"><span class="card-icon" role="img" aria-label="Storm damage cleanup icon"></span><div class="card-label">Storm Damage<br>Cleanup</div></div>
  <div class="abs card" style="left:776px;top:942px"><span class="card-icon" role="img" aria-label="Emergency tree services icon"></span><div class="card-label">Emergency<br>Tree Services</div></div>

  <h2 class="abs about-title">Who We Are</h2>
  <div class="abs about-copy">
    <p>At Corvane Tree Care, we are more than just a tree service company, we are stewards of our beautiful trees. With a passion deeply rooted in arboriculture, we embark on a mission to promote the health, beauty, and safety of your trees and landscapes.</p>
    <p>Whether it's expert tree trimming to enhance aesthetics, meticulous tree removal to mitigate hazards, or comprehensive tree health assessments to ensure safety, we approach each task with unwavering dedication and attention to detail.</p>
  </div>
  <a class="abs btn" style="left:199px;top:1483px;width:118px;height:24px">Get a FREE Estimate</a>

  <div class="abs about-media" role="img" aria-label="Collage of tree work photos: arborist climbing a trunk, fallen tree, chainsaw cutting a log"></div>

  <svg class="abs" style="left:0;top:1190px" width="1146" height="420" viewBox="0 0 1146 420">
    <path d="M124 348 C300 400 500 392 760 392 H1146 V404 H760 C480 404 260 406 132 366 Z" fill="var(--green)"/>
  </svg>

  <section class="abs why" role="img" aria-label="Photo of an arborist in a helmet roped to a tree trunk"></section>
  <div class="abs why-panel">
    <h2 class="why-title">Why Choose Us?</h2>
    <ul class="why-list">
      <li>Licensed and Insured</li>
      <li>24-Hours Emergency Services</li>
      <li>Locally Owned &amp; Operated</li>
      <li>Professional Work</li>
      <li>Safety is Our No.1 Priority</li>
      <li>Free Estimates</li>
      <li>Licensed Arborist on Staff</li>
    </ul>
  </div>

  <footer class="abs footer">
    <div class="abs brand" style="left:199px;top:19px"><span class="brand-mark"></span>Corvane Tree Care</div>
    <div class="phones">
      <svg width="11" height="11" viewBox="0 0 24 24"><path d="M6.6 10.8a15 15 0 006.6 6.6l2.2-2.2c.3-.3.7-.4 1-.2 1.1.4 2.3.6 3.6.6.6 0 1 .4 1 1V20c0 .6-.4 1-1 1A17 17 0 013 4c0-.6.4-1 1-1h3.5c.6 0 1 .4 1 1 0 1.3.2 2.5.6 3.6.1.3 0 .7-.2 1z" fill="var(--green)"/></svg>
      <span>(337) 555-0142&nbsp; (318) 555-0187</span>
    </div>
  </footer>

</main>
</div>
</body>
</html>
```